Business Card Design

Very plain simple card, Plain modern font. Background. Grey fading to black. Large Bright lime green text. Saying.

TWR-ZA.COM

Small other details in white text.

Irish Horse Sales . Livery . Stud . Shows

Mark Dabrowski
TWR
Birch Lodge
Carrowmede Lane
Thistlecombe
Lincolnshire
LN4 7JX

Email. Twrzap@mailvale.co.uk
Tel. 07482 936504

Industry/Entity Type

Business

Contact Information for Business Card

As below

```html
<!DOCTYPE html>
<html lang="en">
<head>
<meta charset="utf-8">
<title>TWR-ZA.COM Business Card</title>
<link rel="stylesheet" href="https://fonts.googleapis.com/css2?family=Didact+Gothic&display=swap">
<style>
  :root {
    --lime: #a8e03a;
    --white: #ffffff;
    --black: #000000;
    --grey: #4e4e4e;
    --card-font: "Didact Gothic", "Century Gothic", sans-serif;
  }
  * { margin: 0; padding: 0; box-sizing: border-box; }
  html, body {
    width: 1200px;
    height: 770px;
    overflow: hidden;
    background: var(--black);
  }
  .card {
    position: relative;
    width: 1200px;
    height: 770px;
    overflow: hidden;
    font-family: var(--card-font);
    color: var(--white);
    background: linear-gradient(215deg, var(--grey) 0%, #262626 38%, #0a0a0a 62%, var(--black) 100%);
  }
  .horse-art {
    position: absolute;
    left: 30px;
    top: 10px;
    width: 740px;
    height: 500px;
  }
  .brand {
    position: absolute;
    left: 44px;
    top: 600px;
    font-size: 78px;
    font-weight: 400;
    line-height: 1;
    color: var(--lime);
    letter-spacing: 1px;
  }
  .services {
    position: absolute;
    left: 48px;
    top: 716px;
    font-size: 26px;
    line-height: 1;
    white-space: nowrap;
  }
  .contact {
    position: absolute;
    left: 634px;
    top: 416px;
    list-style: none;
  }
  .contact__name {
    font-size: 38px;
    line-height: 42px;
    margin-bottom: 20px;
  }
  .contact__line {
    font-size: 33px;
    line-height: 53px;
    white-space: nowrap;
  }
</style>
</head>
<body>
  <main class="card">
    <svg class="horse-art" role="img" aria-label="Lime green line illustration of a leaping horse" viewBox="0 0 740 500">
      <defs>
        <radialGradient id="horseGlow" cx="50%" cy="50%" r="50%">
          <stop offset="0%" stop-color="#a8e03a" stop-opacity="0.16"/>
          <stop offset="55%" stop-color="#a8e03a" stop-opacity="0.07"/>
          <stop offset="100%" stop-color="#a8e03a" stop-opacity="0"/>
        </radialGradient>
      </defs>
      <ellipse cx="390" cy="220" rx="350" ry="230" fill="url(#horseGlow)"/>
    </svg>

    <h1 class="brand">TWR-ZA.COM</h1>
    <p class="services">Irish Horse Sales . Livery . Stud . Shows</p>

    <ul class="contact">
      <li class="contact__name">Mark Dabrowski</li>
      <li class="contact__line">Tel. 07482 936504</li>
      <li class="contact__line">Email. Twrzap@mailvale.co.uk</li>
      <li class="contact__line">Birch Lodge</li>
      <li class="contact__line">Carrowmede Lane</li>
      <li class="contact__line">Thistlecombe Lincolnshire LN4 7JX</li>
    </ul>
  </main>
</body>
</html>
```